Wordpress Business Travel Blog and Discussion Board

Oh, Hello!

We are looking for a motivated designer to create a full, turnkey interactive WordPress website geared toward business travel that includes a news style blog (look at GizmoForge.com and Wirelume.com for the style we like) that is seamlessly integrated with a robust message board (look at JetBanter.com and AirTally.com). Ok, so stick with us here because this is actually a pretty cool project that shouldn't be too hard, but yes, of course we have some curve balls that we are throwing your way. Sorry! :)

*On the front page*

- We would like to have a typical news style blog layout that is fun, somewhat professional, and easy to read. That's easy!

- Somewhere within first glance, we would like to have a short list of the most active discussions on our discussion board. (What's trending, or something like that). Not too bad, right?

- Overall, want to have a good amount of content, but we also do not want the visitor to feel as if he or she is having to sift through a lot of content to see what he or she wants to see. Great! We're past the beginning!

We will have traditional visual advertising on all of our pages. Please leave space as necessary :)

*On the Blog/News story pages*

Let's keep these simple - but there is a twist!

Let's say I create a blog/news post. I would like that blog/news post to also be opened as a discussion on the discussion board. For example, I write an article about Corvane Airways and their service on a particular international flight. This will be opened as a discussion under the Corvane Airways topic in the discussion board. Other users can also open new discussions under any topic on the discussion board, but they cannot post stories (unless permission is given) to the blog wall. We would like their posts to show up as regular discussion board posts while the news/blog posts by us show up as news/blog posts on the front page, *and* (oh yes we did!) as discussions in the discussion board. Of course, users will still be able to post comments to the news/blog post, which will also be posted in the discussion.

OK, does that make sense? Let me know if I can help make this more clear! :) Sorry!

*Wiki Pages*

Take a look at the Corvane Airways example above. In that example, my news/blog entry automatically opens a new discussion post. Although we won't necessarily need to create a new wiki page, we would like to tag the post and the discussion to a wiki page about the topic. The wiki page can be created and edited by all users (and locked by us if necessary). BONUS! Can we tag more than one wiki page?

*Websites that inspire us*

GizmoForge.com - concept and design
Wirelume.com - concept and design
JetBanter.com - concept
AirTally.com - concept
pipwhisper.com - concept

All of the sites above are great and we can only thrive with their great success. We are not aiming to be a competitor to the travel sites, but just another great option for interested visitors. Please do not simply copy what they have. What is posted above is a list of our favorite sites that we visit every day.

Our favorite font is Segoe UI, but please don't use this (or a similar font) too much! Maybe just titles would be great. You're the designer so you can make the call here.

Also, our favorite color is blue, but if you have another favorite color, go ahead and show us what you can do! (Don't use too much blue!)

*Oh, and One More Thing*

(I know, you thought we were done. We're not!)

Here's the killer - We would like to create a way for people to, say, enter the details of their next trip and be matched with someone who will also be on a portion of their trip.

For example, let's say I am flying Halvern Skyways flight 109 from Los Angeles to New York Pellham Airport this Friday. I am staying at the Marlowe Inn Harbor Plaza on Friday night, and I am flying back on Saturday night on Brisko flight 290 from New York Pellham airport back to Los Angeles. Another user will also be on the Brisko flight back to Los Angeles with me and he entered that information in the website. (Note, the user has to manually enter this information). The other user and I will both be notified that there is at least one other user who will be on the same Brisko flight as me. We will both have the option to reveal our online identity - which will in fact be released to each person as long as each person *mutually* agrees.

This can be very simple - almost like a dating site type of match but it is based on two people being in the same place at the same time (based on what they report). Also, we would like to be able to collect this information - not necessarily tied to the user's true identity. The information we would like to have is - what the user is claiming he or she is doing on the trip (i.e. staying at the Marlowe Harbor Plaza, flying Halvern Skyways), and whether or not the user agreed to reveal his or her identity - AND! whether or not the users both revealed their identity.

*Most Important*

HAVE FUN and THANK YOU!! :)

A couple of quick notes - this is a design and code project. We are most likely offering a more $(!) design and code project for the version 2.0 of this website once we get user feedback from this first round.

Also, the name of the website is GoJaunt. (www.gojaunt.example)

Good luck!

Reason: Extending as requested by a few designers. Only 3 more days to get your designs in!

Reason: All designs look great! Last chance for one or two more designers who have requested an extension. All designs that were already submitted on time will be considered with much higher priority. Thank you!

Requirements
Must have
• We need to have a high end, professional, modern, and clean design on the front page to entice readers to constantly visit and stay on our site.
Nice to have
• It would be great to give us the ability to automatically recognize users for visiting the website and/or participating and commenting. Social badges, recognition, etc. would be very cool.
Should not have
• Although this is a website around business travel, we do not necessarily want it to be business travel themed. There can be hints of the theme, but otherwise the visual look should be somewhat generic.

```html
<!DOCTYPE html>
<html lang="en">
<head>
<meta charset="utf-8">
<title>Tessaly Journeys</title>
<link href="https://fonts.googleapis.com/css2?family=Open+Sans:wght@400;600;700&family=Droid+Sans&display=swap" rel="stylesheet">
<style>
:root{
  --navy:#2f4763;
  --navy-dark:#223850;
  --orange:#e8731f;
  --text:#4a4a4a;
  --muted:#8a8a8a;
  --line:#e2e2e2;
  --panel:#f3f3f3;
  --side:#e9e9e9;
  --fb:#1f6aa8;
  --sky1:#9cc6ea;
  --sky2:#dcebf7;
}
*{margin:0;padding:0;box-sizing:border-box}
html,body{width:780px;height:1200px;overflow:hidden}
body{position:relative;background:#f6f6f6;font-family:"Open Sans",Arial,sans-serif;color:var(--text)}
.abs{position:absolute}
.topbar{left:0;top:0;width:780px;height:31px;background:linear-gradient(#4a6180,var(--navy-dark))}
.social-dots{left:481px;top:6px;display:flex;gap:8px}
.social-dots span{width:19px;height:19px;border-radius:50%;background:#2d7fd0;border:2px solid #cfe1f3}
.social-dots span:last-child{background:var(--orange);border-color:#f7d2b3}
.toplinks{left:572px;top:9px;font-size:8px;font-weight:600;color:#fff;letter-spacing:.2px;white-space:nowrap}
.toplinks b{font-weight:400;margin:0 6px;color:#9fb2c8}
.header{left:0;top:31px;width:780px;height:116px;background:linear-gradient(#f2f2f2,#fafafa)}
.logo{left:60px;top:50px;font-size:24px;font-weight:600;color:var(--navy);white-space:nowrap}
.slogan{left:172px;top:83px;font-size:8.5px;color:#666}
.search{left:572px;top:62px;width:148px;height:17px;background:#fff;border:1px solid #d5d5d5;font-size:7px;font-style:italic;color:#aaa;padding:4px 0 0 12px}
.nav{left:60px;top:109px;width:660px;height:37px;display:flex;justify-content:space-between;border-top:1px solid var(--line)}
.nav div{font-size:8.5px;color:#333;padding:0 14px;line-height:37px;position:relative;white-space:nowrap}
.nav div+div::before{content:"";position:absolute;left:0;top:10px;height:18px;border-left:1px solid #ddd}
.nav .on{background:var(--navy);color:#fff;border-radius:4px 4px 0 0}
.navline{left:0;top:145px;width:780px;height:2px;background:var(--navy)}
.hero{left:63px;top:153px;width:656px;height:193px;background:linear-gradient(180deg,var(--sky1),var(--sky2));border:1px solid #fff;box-shadow:0 4px 6px rgba(0,0,0,.12)}
.hero-photo{left:0;top:0;width:245px;height:191px;background:linear-gradient(90deg,#c9b29a,#e2cfb9 60%,rgba(220,235,247,0))}
.hero h2{left:259px;top:56px;font-size:20px;font-weight:400;color:#fff;font-family:"Droid Sans",sans-serif;white-space:nowrap}
.hero p{left:259px;top:91px;width:272px;font-size:7.5px;line-height:12px;color:#2b3a48}
.dots{left:582px;top:170px;display:flex;gap:9px}
.dots i{width:8px;height:8px;border-radius:50%;background:#fff}
.dots i.on{background:var(--orange)}
.main{left:60px;top:372px;width:468px;height:708px;background:#fff}
.sidebar{left:534px;top:372px;width:186px;height:708px;background:var(--side)}
.welcome{left:68px;top:383px;font-size:17px;color:var(--orange);font-weight:400}
.intro{left:68px;top:412px;width:450px;font-size:7.6px;line-height:15px;color:#555;text-align:justify}
.sep{left:68px;top:487px;width:450px;height:1px;background:var(--line)}
.blog-h{left:68px;top:499px;font-size:12px;color:var(--orange);display:flex;align-items:center;gap:10px}
.post{left:67px;width:453px;height:126px;background:var(--panel)}
.post .thumb{position:absolute;left:9px;top:16px;width:106px;height:64px;border:2px solid #fff;box-shadow:0 0 2px #aaa}
.post h3{position:absolute;left:129px;top:12px;font-size:9.6px;font-weight:600;color:#333}
.post p{position:absolute;left:129px;top:29px;width:313px;font-size:7.6px;line-height:12.8px;color:#555;text-align:justify}
.post .share{position:absolute;left:10px;top:94px;display:flex;gap:3px;font-size:6.5px}
.share span{border:1px solid #ccc;background:#fff;padding:1px 3px}
.share .btn{background:#eef2f7;font-weight:700;color:#3a5a8a}
.post .meta{position:absolute;left:129px;top:89px;width:312px;height:23px;background:#fff;font-size:7.6px;display:flex;align-items:center;padding-left:14px;gap:22px;color:#444;white-space:nowrap}
.meta em{font-style:normal;color:var(--orange)}
.meta .rm{display:flex;align-items:center;gap:6px}
.pager{left:281px;top:1047px;display:flex;gap:3px;font-size:6.5px;align-items:center;color:#555;white-space:nowrap}
.pager span{width:14px;height:14px;background:#ddd;border-radius:2px;text-align:center;line-height:14px;color:#999}
.pager span.on{background:#999;color:#fff}
.news{left:544px;top:385px;width:169px;height:85px;background:linear-gradient(#5b7595,#3f5878);border-radius:5px;border:2px solid #b9c6d5}
.news h4{position:absolute;left:40px;top:11px;font-size:11.5px;font-weight:400;color:#fff;white-space:nowrap}
.news .env{position:absolute;left:9px;top:7px}
.news .field{position:absolute;left:8px;top:39px;width:150px;height:17px;background:#fff;font-size:6.5px;font-style:italic;color:#aaa;padding:4px 0 0 10px;border-radius:2px}
.news .submit{position:absolute;left:114px;top:64px;width:47px;height:13px;background:linear-gradient(#fff,#ccc);border-radius:7px;font-size:6.5px;font-style:italic;text-align:center;line-height:13px;color:#345}
.trend{left:544px;top:480px;width:169px;height:293px;background:#fff;border-radius:4px}
.trend h4{position:absolute;left:38px;top:12px;font-size:11.5px;font-weight:400;color:var(--orange)}
.trend .bar{position:absolute;left:0;top:38px;width:169px;height:1px;background:var(--line)}
.titem{position:absolute;left:8px;width:158px}
.titem .av{position:absolute;left:0;top:2px;width:20px;height:20px}
.titem p{position:absolute;left:29px;top:0;width:128px;font-size:6.8px;line-height:12.3px;color:#555;text-align:justify}
.titem a{color:#c0392b;text-decoration:underline}
.fb{left:544px;top:784px;width:176px;height:160px;background:#fff}
.fb .head{position:absolute;left:0;top:0;width:176px;height:28px;background:var(--fb);color:#fff;font-size:11.5px;font-weight:600;padding:6px 0 0 41px}
.fb .icon{position:absolute;left:12px;top:5px;width:18px;height:18px;border-radius:50%;border:2px solid #fff}
.fb .count{position:absolute;left:9px;top:44px;font-size:5.8px;color:#666}
.fb .like{position:absolute;left:80px;top:41px;width:53px;height:12px;border:1px solid #ccc;background:#f2f2f2;font-size:5.8px;padding:2px 5px}
.faces{position:absolute;left:9px;top:62px;display:grid;grid-template-columns:repeat(4,32px);column-gap:8px;row-gap:14px}
.face{width:32px;height:32px;position:relative}
.face span{position:absolute;top:35px;left:0;width:32px;text-align:center;font-size:5.2px;color:#666}
.ad{left:544px;top:960px;width:169px;height:103px}
.footer{left:0;top:1093px;width:780px;height:107px;background:#ebebeb}
.fcol h5{font-size:8.6px;font-weight:600;color:#333}
.about p{width:175px;font-family:Arial,Helvetica,sans-serif;font-size:8px;line-height:13.5px;color:#444;margin-top:9px}
.links{display:grid;grid-template-columns:65px 69px 50px;row-gap:8px;margin-top:11px;font-size:7.6px;color:#888;white-space:nowrap}
.fsoc{display:flex;gap:8px;margin-top:11px}
.fsoc span{width:19px;height:19px;border-radius:3px}
.legal{font-family:Arial,Helvetica,sans-serif;font-size:8px;color:#555;margin-top:9px;line-height:14px;white-space:nowrap}
.legal .c{color:#999}
.vdiv{top:1108px;width:0;height:78px;border-left:1px dotted #bbb}
</style>
</head>
<body>
<div class="abs topbar"></div>
<div class="abs social-dots"><span></span><span></span><span></span></div>
<div class="abs toplinks">SIGN IN<b>|</b>REGISTER<b>|</b>HELP<b>|</b>FAQ</div>

<div class="abs header"></div>
<div class="abs logo">Tessaly Journeys</div>
<div class="abs slogan">Company Slogan Goes here!</div>
<div class="abs search">Search</div>
<div class="abs nav">
  <div class="on">HOME</div><div>ABOUT</div><div>BLOG</div><div>FORUMS</div><div>SERVICES</div><div>CITIES</div><div>WHATS TRENDING</div><div>TESTIMONIALS</div><div>CONTACT</div>
</div>
<div class="abs navline"></div>

<section class="abs hero">
  <div class="abs hero-photo" role="img" aria-label="Photo of a smiling family of three"></div>
  <h2 class="abs">Nemo enim ipsam voluptatem</h2>
  <p class="abs">Sed ut perspiciatis unde omnis iste natus error sit voluptatem accusantium doloremque laudantium, totam rem aperiam, eaque ipsa quae ab illo inventore veritatis et quasi</p>
  <div class="abs dots"><i></i><i class="on"></i><i></i><i></i></div>
</section>

<div class="abs main"></div>
<div class="abs sidebar"></div>

<h1 class="abs welcome">Welcome to our site</h1>
<p class="abs intro">Sed ut perspiciatis unde omnis iste natus error sit voluptatem accusantium doloremque laudantium, totam rem aperiam, eaque ipsa quae ab illo inventore veritatis et quasi architecto beatae vitae dicta sunt explicabo. Nemo enim ipsam voluptatem quia voluptas sit aspernatur aut odit aut fugit, sed quia consequuntur magni dolores eos qui ratione voluptatem sequi nesciunt. Neque porro quisquam est, qui dolorem ipsum quia dolor sit amet.</p>
<div class="abs sep"></div>
<div class="abs blog-h">
  <svg width="22" height="16" viewBox="0 0 22 16"><path d="M2 6h5l10-5v14L7 10H2z" fill="#e0652a"/><rect x="4" y="10" width="3" height="5" fill="#b34d1c"/></svg>Blog
</div>

<article class="abs post" style="top:530px">
  <div class="thumb" style="background:linear-gradient(#5d8fc4,#e9d4b4)" role="img" aria-label="Photo of a passenger jet in flight"></div>
  <h3>Quis autem vel eumiure reprehenderit</h3>
  <p>Totam rem aperiam, eaque ipsa quae ab illo inventore veritatis et quasi architecto beatae vitae dicta sunt explicabo. Nemo enim ipsam voluptatem quia voluptas sit aspernatur aut odit aut fugit, sed quia consequuntur magni dolores eos qui ratione voluptatem sequi nesciunt.</p>
  <div class="share"><span class="btn">Like</span><span>3k</span><span class="btn">Share</span><span>316</span></div>
  <div class="meta"><span class="rm"><svg width="13" height="9"><ellipse cx="6.5" cy="4" rx="6.5" ry="4" fill="#e8902f"/></svg><em>Read More</em></span><span>Posted by <em>Ione Carrow</em></span><span>Tags: <em>Travel, Places</em></span></div>
</article>

<article class="abs post" style="top:660px">
  <div class="thumb" style="background:linear-gradient(#6fb0d8,#33b3b0)" role="img" aria-label="Photo of overwater villas in a turquoise lagoon"></div>
  <h3>Quis autem vel eumiure reprehenderit</h3>
  <p>Totam rem aperiam, eaque ipsa quae ab illo inventore veritatis et quasi architecto beatae vitae dicta sunt explicabo. Nemo enim ipsam voluptatem quia voluptas sit aspernatur aut odit aut fugit, sed quia consequuntur magni dolores eos qui ratione voluptatem sequi nesciunt.</p>
  <div class="share"><span class="btn">Like</span><span>3k</span><span class="btn">Share</span><span>316</span></div>
  <div class="meta"><span class="rm"><svg width="13" height="9"><ellipse cx="6.5" cy="4" rx="6.5" ry="4" fill="#e8902f"/></svg><em>Read More</em></span><span>Posted by <em>Ione Carrow</em></span><span>Tags: <em>Travel, Places</em></span></div>
</article>

<article class="abs post" style="top:789px">
  <div class="thumb" style="background:linear-gradient(#8ec3e6,#2e8fc0 70%,#e6e6e6)" role="img" aria-label="Photo of a couple sitting by the sea"></div>
  <h3>Quis autem vel eumiure reprehenderit</h3>
  <p>Totam rem aperiam, eaque ipsa quae ab illo inventore veritatis et quasi architecto beatae vitae dicta sunt explicabo. Nemo enim ipsam voluptatem quia voluptas sit aspernatur aut odit aut fugit, sed quia consequuntur magni dolores eos qui ratione voluptatem sequi nesciunt.</p>
  <div class="share"><span class="btn">Like</span><span>3k</span><span class="btn">Share</span><span>316</span></div>
  <div class="meta"><span class="rm"><svg width="13" height="9"><ellipse cx="6.5" cy="4" rx="6.5" ry="4" fill="#e8902f"/></svg><em>Read More</em></span><span>Posted by <em>Ione Carrow</em></span><span>Tags: <em>Travel, Places</em></span></div>
</article>

<article class="abs post" style="top:918px">
  <div class="thumb" style="background:linear-gradient(90deg,#b07a5a,#d9c3a5,#7f8f9a)" role="img" aria-label="Photo of two travellers reading beside a bus"></div>
  <h3>Quis autem vel eumiure reprehenderit</h3>
  <p>Totam rem aperiam, eaque ipsa quae ab illo inventore veritatis et quasi architecto beatae vitae dicta sunt explicabo. Nemo enim ipsam voluptatem quia voluptas sit aspernatur aut odit aut fugit, sed quia consequuntur magni dolores eos qui ratione voluptatem sequi nesciunt.</p>
  <div class="share"><span class="btn">Like</span><span>3k</span><span class="btn">Share</span><span>316</span></div>
  <div class="meta"><span class="rm"><svg width="13" height="9"><ellipse cx="6.5" cy="4" rx="6.5" ry="4" fill="#e8902f"/></svg><em>Read More</em></span><span>Posted by <em>Ione Carrow</em></span><span>Tags: <em>Travel, Places</em></span></div>
</article>

<div class="abs pager">Page 1 of 32&nbsp;<span class="on">1</span><span>2</span><span>3</span><span>4</span><span>5</span><span>6</span><span>7</span><span>8</span><span>»</span>&nbsp;…&nbsp;<span>»»</span></div>

<aside class="abs news">
  <svg class="env" width="26" height="22" viewBox="0 0 26 22"><rect x="1" y="5" width="24" height="16" rx="2" fill="#f0c45a"/><path d="M1 7l12 8 12-8" fill="none" stroke="#c9962d" stroke-width="1.5"/></svg>
  <h4>Newsletter Subscribe</h4>
  <div class="field">Enter your mail ID</div>
  <div class="submit">SUBMIT</div>
</aside>

<aside class="abs trend">
  <svg style="position:absolute;left:8px;top:10px" width="22" height="20" viewBox="0 0 22 20"><rect x="1" y="5" width="20" height="14" rx="2" fill="#c8862e"/><rect x="7" y="1" width="8" height="5" rx="1" fill="none" stroke="#8a5a1c" stroke-width="2"/></svg>
  <h4>Whats Trending</h4>
  <div class="bar"></div>
  <div class="titem" style="top:50px"><div class="av" style="background:#3f9fd0"></div><p>Name minus libero tempore, soluta nobis nihil impedit est eligendi optio cumque <a>http://www.velmora.example/ ut/labore/4et</a>.</p></div>
  <div class="titem" style="top:112px"><div class="av" style="background:#6d5555"></div><p>Name minus libero tempore, soluta nobis nihil impedit est eligendi optio cumque <a>http://www.velmora.example/ ut/labore/4et</a>.</p></div>
  <div class="titem" style="top:172px"><div class="av" style="background:#3f9fd0"></div><p>Name minus libero tempore, soluta nobis nihil impedit est eligendi optio cumque <a>http://www.velmora.example/ ut/labore/4et</a>.</p></div>
  <div class="titem" style="top:234px"><div class="av" style="background:#6d5555"></div><p>Name minus libero tempore, soluta nobis nihil impedit est eligendi optio cumque <a>http://www.velmora.example/ ut/labore/4et</a>.</p></div>
</aside>

<aside class="abs fb">
  <div class="head">Friends Feed</div><div class="icon"></div>
  <div class="count">347 people like</div>
  <div class="like">Like</div>
  <div class="faces">
    <div class="face" style="background:#8aa7b8" role="img" aria-label="Member photo"><span>Rina</span></div>
    <div class="face" style="background:#5f8a9a" role="img" aria-label="Member photo"><span>Tomas</span></div>
    <div class="face" style="background:#6f7d52" role="img" aria-label="Member photo"><span>Oren</span></div>
    <div class="face" style="background:#d9c9c9" role="img" aria-label="Member avatar"><span>Milo</span></div>
    <div class="face" style="background:#3a3a3a" role="img" aria-label="Member photo"><span>Dario</span></div>
    <div class="face" style="background:#7c7f83" role="img" aria-label="Member photo"><span>Jonah</span></div>
    <div class="face" style="background:#e4e4e4" role="img" aria-label="Member avatar"><span>Pavel</span></div>
    <div class="face" style="background:#9a9a9a" role="img" aria-label="Member photo"><span>Ellis</span></div>
  </div>
</aside>

<div class="abs ad" role="img" aria-label="Music advertisement: new single available on Tunevault and Melodeck" style="background:linear-gradient(90deg,#fff 45%,#e03a2a 70%,#2a1a18)"></div>

<footer class="abs footer"></footer>
<div class="abs fcol about" style="left:76px;top:1108px"><h5>About Tessaly Journeys</h5><p>There are many variations of passages of Lorem Ipsum available, but the majority have suffered alteration in some form, by injected humour, or randomised</p></div>
<div class="abs vdiv" style="left:262px"></div>
<div class="abs fcol" style="left:294px;top:1108px"><h5>QUICK LINKS</h5>
  <div class="links"><span>Home</span><span>About us</span><span>Blog</span><span>Forums</span><span>Services</span><span>Cities</span><span>Whats trending</span><span>Testimonials</span><span>Contact us</span></div></div>
<div class="abs vdiv" style="left:500px"></div>
<div class="abs fcol" style="left:523px;top:1108px"><h5>CONNECT WITH US</h5>
  <div class="fsoc"><span style="background:#3b67a8"></span><span style="background:#49a7d8"></span><span style="background:#e8731f"></span><span style="background:#4aa236"></span><span style="background:#5dbb3a"></span></div>
  <div class="legal">Terms of Service | &nbsp;Privacy Policy<br><span class="c">© 2010 - 2011 Tessaly Journeys. All Rights Reserved</span></div></div>
</body>
</html>
```